BRL business card

For a business card with our logo

Contact Information for Business Card

Mathéo VRANEL
Founder & CEO
email : ceo@brightlanterncollective.com / www.brightlanterncollective.com /
instagram / facebook / WhatsApp
N°: +590 690 482 517

Colors

Designer to choose colors to be used in the design.

```html
<!DOCTYPE html>
<html lang="en">
<head>
<meta charset="utf-8">
<title>BRL business card</title>
<link rel="stylesheet" href="https://fonts.googleapis.com/css2?family=Lato:wght@400;700&display=swap">
<style>
  :root {
    --backdrop: #2b2b2d;
    --orange: #f04a12;
    --blue: #1a2fc4;
    --navy: #1c2a9c;
    --paper: #f7f7f7;
    --ink: #1d1d1d;
    --panel-line: #e4e4e4;
  }
  * { box-sizing: border-box; margin: 0; padding: 0; }
  html, body { width: 1200px; height: 997px; overflow: hidden; }
  body {
    background: var(--backdrop);
    font-family: "Lato", sans-serif;
    position: relative;
  }
  .card {
    position: absolute;
    left: 320px;
    width: 560px;
    height: 320px;
    border-radius: 2px;
    box-shadow: 0 14px 34px rgba(0,0,0,.45);
    overflow: hidden;
  }

  /* Front */
  .card-front { top: 110px; background: var(--orange); }
  .front-brand {
    position: absolute; inset: 0;
    display: flex; align-items: center; justify-content: center; gap: 18px;
  }
  .brand-dot {
    width: 78px; height: 78px; border-radius: 50%;
    background: #fff; flex: none;
  }
  .brand-dot.small { width: 52px; height: 52px; background: var(--orange); }
  .brand-name {
    font-family: "Lato", sans-serif;
    font-weight: 700;
    letter-spacing: .08em;
    line-height: 1.15;
  }
  .front-brand .brand-name { color: #fff; font-size: 26px; }

  /* Back */
  .card-back { top: 520px; background: var(--paper); }
  .panel-line {
    position: absolute; top: 0; width: 1px; height: 166px;
    background: var(--panel-line);
  }
  .back-brand {
    position: absolute; top: 38px; left: 0; right: 0;
    display: flex; align-items: center; justify-content: center; gap: 12px;
  }
  .back-brand .brand-name { color: var(--navy); font-size: 17px; }
  .rule {
    position: absolute; left: 200px; right: 22px; top: 166px;
    height: 1.5px; background: var(--orange);
  }
  .person { position: absolute; left: 30px; top: 172px; }
  .person-name { color: var(--blue); font-weight: 700; font-size: 21px; line-height: 1.2; }
  .person-role { color: var(--orange); font-size: 15px; margin-top: 2px; }
  .contact-list { position: absolute; left: 30px; top: 226px; list-style: none; }
  .contact-list li {
    display: flex; align-items: center; gap: 9px;
    font-size: 13.5px; color: var(--ink); margin-bottom: 6px;
  }
  .contact-icon { width: 16px; height: 16px; flex: none; }
  .social-list { position: absolute; right: 22px; top: 184px; list-style: none; }
  .social-list li {
    display: flex; align-items: center; gap: 8px;
    font-size: 12.5px; color: var(--ink); margin-bottom: 4px;
  }
  .social-mark { width: 14px; height: 14px; border-radius: 50%; background: var(--navy); flex: none; }
  .footer-bands { position: absolute; left: 0; bottom: 0; width: 560px; height: 100px; }
  .website {
    position: absolute; right: 26px; bottom: 26px;
    color: #fff; font-weight: 700; font-size: 14px; letter-spacing: .02em;
    line-height: 1;
  }
</style>
</head>
<body>

<section class="card card-front" aria-label="Card front">
  <div class="front-brand">
    <span class="brand-dot"></span>
    <span class="brand-name">BRIGHT LANTERN<br>COLLECTIVE</span>
  </div>
</section>

<section class="card card-back" aria-label="Card back">
  <span class="panel-line" style="left:187px"></span>
  <span class="panel-line" style="left:373px"></span>

  <div class="back-brand">
    <span class="brand-dot small"></span>
    <span class="brand-name">BRIGHT LANTERN<br>COLLECTIVE</span>
  </div>

  <div class="rule"></div>

  <div class="person">
    <p class="person-name">Mathéo VRANEL</p>
    <p class="person-role">Founder &amp; CEO</p>
  </div>

  <ul class="contact-list">
    <li>
      <svg class="contact-icon" viewBox="0 0 16 16" aria-hidden="true">
        <circle cx="8" cy="8" r="8" fill="var(--orange)"/>
        <path d="M5.2 4.2c.5-.3 1-.2 1.2.3l.6 1.3c.2.4 0 .8-.3 1l-.5.4c.4.9 1.1 1.6 2 2l.4-.5c.3-.3.7-.4 1-.2l1.3.6c.5.2.6.8.3 1.2-.6.9-1.6 1.2-2.6.7-1.6-.8-2.9-2.1-3.6-3.7-.4-1-.1-2 .2-2.6z" fill="#fff"/>
      </svg>
      +590 690 482 517
    </li>
    <li>
      <svg class="contact-icon" viewBox="0 0 16 16" aria-hidden="true">
        <circle cx="8" cy="8" r="8" fill="var(--orange)"/>
        <rect x="4" y="5.2" width="8" height="5.6" rx=".6" fill="none" stroke="#fff" stroke-width="1.1"/>
        <path d="M4.3 5.6 8 8.4l3.7-2.8" fill="none" stroke="#fff" stroke-width="1.1"/>
      </svg>
      ceo@brightlanterncollective.com
    </li>
  </ul>

  <ul class="social-list">
    <li><span class="social-mark"></span>brightlanterncollective</li>
    <li><span class="social-mark"></span>brightlanterncollective</li>
  </ul>

  <svg class="footer-bands" viewBox="0 0 560 100" aria-hidden="true">
    <path d="M0 80 H206 C222 80 228 66 238 58 L243 62 C232 72 226 87 208 87 H0 Z" fill="var(--blue)"/>
    <path d="M0 92 H226 C248 92 252 44 292 44 H560 V100 H0 Z" fill="var(--orange)"/>
  </svg>
  <p class="website">www.brightlanterncollective.com</p>
</section>

</body>
</html>
```